Brevane Advisory business card

Premium business card required
I have attached the brand as a powerpoint template but this can be made to look very up market, I have also attached my BIO for title reasons and to give you a feel for my skills
front of card
Darrel Voskuij
Managing Director Brevane Advisory
Retail, Customer-Led Experience, Transformation and Maximising Shareholder Return
Mobile +61(0)487395028
Email darrelbrevaneadvisory.example
back of card

BREVANE ADVISORY’ OFFERING

We transform customer environments to extract benefits while elevating service levels;
We release millions of dollars in self-funding through continuous improvement;
We see CX as a key differentiator, proactively guarding share from market disrupters;
We re-invent service and create front-end of the future.

```html
<!DOCTYPE html>
<html lang="en">
<head>
<meta charset="utf-8">
<title>Brevane Advisory business card</title>
<link href="https://fonts.googleapis.com/css2?family=Questrial&family=Montserrat:wght@500;600&display=swap" rel="stylesheet">
<style>
  :root{
    --bg:#3a3536;
    --paper:#f7f7f5;
    --ink:#2b2b2b;
    --grey:#555;
    --gold:#c8a62a;
    --dark:#232323;
    --white:#ffffff;
  }
  *{box-sizing:border-box;margin:0;padding:0}
  html,body{width:1200px;height:901px;overflow:hidden;background:var(--bg)}
  body{position:relative;font-family:"Questrial",sans-serif}
  .card{position:absolute;left:240px;width:720px;height:412px;overflow:hidden;box-shadow:0 10px 30px rgba(0,0,0,.45)}
  .card--front{top:24px;background:var(--paper)}
  .card--back{top:476px;background:var(--dark)}

  .accent-dot{position:absolute;right:-46px;top:58px;width:92px;height:92px;border-radius:50%;background:var(--gold)}
  .holder{position:absolute;right:80px;top:78px;text-align:right}
  .holder__name{font-family:"Montserrat",sans-serif;font-weight:600;font-size:31px;color:var(--gold);letter-spacing:.5px}
  .holder__title{font-size:15px;color:var(--grey);margin-top:2px}
  .rule{position:absolute;height:1px;background:var(--gold)}
  .rule--title{left:330px;right:70px;top:150px}
  .rule--contact{left:55px;width:360px;top:244px}

  .brand{position:absolute;left:55px;top:170px;display:flex;align-items:center;gap:12px}
  .brand__mark{width:46px;height:46px;border-radius:50%;background:var(--ink)}
  .brand__name{font-family:"Montserrat",sans-serif;font-weight:600;font-size:34px;color:var(--ink)}

  .contacts{position:absolute;left:55px;top:256px;list-style:none}
  .contacts li{display:flex;align-items:center;gap:10px;font-size:17px;color:var(--ink);line-height:24px}
  .contacts svg{width:14px;height:14px;flex:none}

  .tagline{position:absolute;left:55px;top:344px;font-family:"Montserrat",sans-serif;font-weight:600;font-size:9.5px;letter-spacing:.4px;color:var(--ink);text-transform:uppercase}
  .band{position:absolute;left:0;bottom:0;width:720px;height:50px}

  .offer{position:absolute;left:60px;top:52px;right:60px}
  .offer__heading{font-family:"Montserrat",sans-serif;font-weight:600;font-size:20px;color:var(--white);letter-spacing:1px;text-transform:uppercase}
  .offer__rule{height:1px;background:var(--gold);width:420px;margin:12px 0 26px}
  .offer__list{list-style:none}
  .offer__list li{display:flex;align-items:flex-start;gap:18px;font-family:"Montserrat",sans-serif;font-weight:500;font-size:16px;line-height:21px;color:var(--gold);margin-bottom:16px}
  .offer__bullet{width:18px;height:18px;border-radius:50%;background:var(--white);flex:none;margin-top:10px}
</style>
</head>
<body>

<section class="card card--front" aria-label="Card front">
  <div class="accent-dot"></div>
  <div class="holder">
    <p class="holder__name">Darrel Voskuij</p>
    <p class="holder__title">Managing Director Brevane Advisory</p>
  </div>
  <div class="rule rule--title"></div>

  <div class="brand">
    <span class="brand__mark"></span>
    <span class="brand__name">Brevane Advisory</span>
  </div>

  <div class="rule rule--contact"></div>
  <ul class="contacts">
    <li><svg viewBox="0 0 14 14"><rect x="3" y="1" width="8" height="12" rx="1.5" fill="none" stroke="var(--gold)" stroke-width="1.4"/></svg>+61(0)487395028</li>
    <li><svg viewBox="0 0 14 14"><rect x="1" y="3" width="12" height="8" fill="var(--gold)"/><path d="M1 3 L7 8 L13 3" fill="none" stroke="var(--paper)" stroke-width="1.2"/></svg>darrel@brevaneadvisory.example</li>
    <li><svg viewBox="0 0 14 14"><circle cx="7" cy="7" r="6" fill="var(--gold)"/><path d="M1 7h12M7 1c-3 3-3 9 0 12M7 1c3 3 3 9 0 12" fill="none" stroke="var(--paper)" stroke-width=".9"/></svg>darrelbrevaneadvisory.example</li>
  </ul>

  <p class="tagline">Retail, Customer-Led Experience, Transformation and Maximising Shareholder Return</p>

  <svg class="band" viewBox="0 0 720 50" preserveAspectRatio="none">
    <polygon points="520,14 720,14 720,30 505,30" fill="var(--gold)"/>
    <rect x="0" y="30" width="720" height="20" fill="var(--dark)"/>
  </svg>
</section>

<section class="card card--back" aria-label="Card back">
  <div class="offer">
    <h2 class="offer__heading">Brevane Advisory’ Offering</h2>
    <div class="offer__rule"></div>
    <ul class="offer__list">
      <li><span class="offer__bullet"></span>We transform customer environments to extract<br>benefits while elevating service levels;</li>
      <li><span class="offer__bullet"></span>We release millions of dollars in self-funding<br>through continuous improvement;</li>
      <li><span class="offer__bullet"></span>We see CX as a key differentiator, proactively<br>guarding share from market disrupters;</li>
      <li><span class="offer__bullet" style="margin-top:2px"></span>We re-invent service and create front-end of the future.</li>
    </ul>
  </div>
</section>

</body>
</html>
```